FLyer for Malaysia's No. 1 Healthcare Job Site (name of job site: Varenta)

Objective of flyer - to get people to register on the job site
Must have:
Logo and Name (Varenta)
Tagline: Malaysia's #1 Healthcare Job site
url: www.varenta-jobs.example
social media links
FB:Varenta
LinkedIn: varentajobs
Instagram: @varentajobs

WE cover the entire healthcare industry areas (doctors, nurses, dentists, pharmacists, psychologists, administrative staff, biomedical engineers....etc)

Please remember that our focus service is our Job-site, we want people to realize in the first look that we are a healthcare Job site.

Flyer size: A5

Color code: #279582 (80%) & #96c836 (20%)

Target Market(s)

All Healthcare Professionals in Malaysia

Industry/Entity Type

Healthcare

Requirements
Must have
• Web site: www.varenta-jobs.example
• Logo and Tagline (attached)
• 2 side design
• Really important (Our Product is our Job site)
Nice to have
• Asian Healthcare professionals, info graphic icons.

```html
<!DOCTYPE html>
<html lang="en">
<head>
<meta charset="utf-8">
<title>Varenta Healthcare Jobs Flyer</title>
<link href="https://fonts.googleapis.com/css2?family=Philosopher:wght@400;700&family=Roboto+Condensed:wght@400;700&family=Archivo+Black&family=Quicksand:wght@400;500&family=Tinos&display=swap" rel="stylesheet">
<style>
:root{
  --teal:#279582;
  --teal-dark:#1e6f61;
  --green:#96c836;
  --green-dark:#7aa829;
  --ink:#1d1d1d;
  --paper:#ffffff;
}
*{margin:0;padding:0;box-sizing:border-box}
html,body{width:1200px;height:857px;overflow:hidden;background:#fff}
.canvas{position:relative;width:1200px;height:857px;background:#fff}
.side{position:absolute;top:16px;width:576px;height:826px;overflow:hidden}
.side--front{left:16px;background:var(--teal)}
.side--back{left:606px;background:var(--green)}
.abs{position:absolute}

/* FRONT */
.front-sheet{left:12px;top:12px;width:552px;height:802px;background:var(--paper);border-radius:80px 0 0 0;overflow:hidden}
.workspace-photo{left:0;top:0;width:552px;height:294px;background:linear-gradient(160deg,#f4f6f6 0%,#dfe5e6 55%,#c9d3d5 100%);opacity:.9}
.brand{left:120px;top:205px;display:flex;align-items:center;gap:22px}
.brand-dot{width:38px;height:38px;border-radius:50%;background:var(--teal)}
.brand-name{font-family:'Philosopher',sans-serif;font-size:74px;color:var(--teal);letter-spacing:2px;line-height:1}
.tagline-top{left:301px;top:306px;font-family:'Philosopher',sans-serif;font-size:31px;color:var(--green-dark)}
.tagline{left:115px;top:344px;font-family:'Philosopher',sans-serif;font-size:36px;color:var(--teal);white-space:nowrap}
.tagline .slash{color:var(--green);font-size:44px;font-weight:700}
.url-button{border-radius:16px;background:linear-gradient(180deg,#7cc5b6 0%,var(--teal) 35%,var(--teal-dark) 100%);box-shadow:0 6px 10px rgba(0,0,0,.18);display:flex;align-items:center;justify-content:center;font-family:'Archivo Black',sans-serif;color:#fff;text-shadow:2px 2px 3px rgba(0,0,0,.35);white-space:nowrap}
.front .url-button{left:72px;top:418px;width:442px;height:88px;font-size:27px}
.cursor{width:40px;height:46px}
.front-waves{left:0;top:560px;width:552px;height:242px}
.quote{left:18px;top:570px;width:290px;text-align:center;font-family:'Roboto Condensed',sans-serif;font-weight:700;color:#fff;line-height:1}
.quote .q1{font-size:19px}
.quote .q2{font-size:28px;margin-top:3px}
.quote .q3{font-size:36px;margin-top:1px}
.steps{left:284px;top:572px;width:184px;height:184px;border-radius:50%;background:var(--green);border:4px solid var(--teal)}
.step{position:absolute;font-family:'Tinos',serif;color:#fff;display:flex;align-items:center;gap:3px}
.step .num{font-size:38px;color:var(--teal-dark);line-height:1}
.step .label{font-size:13px;line-height:1}
.seeker-photo{left:424px;top:588px;width:128px;height:214px;background:linear-gradient(180deg,#e9d4c6 0%,#f6f3f1 60%,#e6eceb 100%);border-radius:64px 0 0 0}
.socials{font-family:'Quicksand',sans-serif;font-size:17px;color:#333;line-height:20px}
.socials li{list-style:none;display:flex;align-items:center;gap:10px}
.socials .chip{width:13px;height:13px;display:inline-block}
.chip--web{border:1.5px solid var(--green);border-radius:50%}
.chip--fb{background:#3b5998}
.chip--in{background:#0e76a8}
.chip--ig{background:#c13584}
.chip--gp{background:#d34836}
.front .socials{left:46px;top:682px}

/* BACK */
.back-sheet{left:12px;top:12px;width:552px;height:802px;background:var(--paper);border-radius:0 90px 0 0;overflow:hidden}
.photo{position:absolute;left:0}
.photo--pharmacist{top:0;width:201px;height:209px;background:linear-gradient(135deg,#d8e6ee,#f3efe6 60%,#e7c9b8)}
.photo--lab{top:213px;width:185px;height:189px;background:linear-gradient(135deg,#2d4fa6,#9fb7cf 50%,#e4ecef)}
.photo--doctor{top:410px;width:229px;height:196px;background:linear-gradient(135deg,#cfd8d6,#f1f3f2 55%,#7e6350)}
.photo--xray{top:614px;width:229px;height:188px;background:linear-gradient(135deg,#3f8f88,#27384a 45%,#e8d9d3)}
.ask{font-family:'Roboto Condensed',sans-serif;color:var(--teal);font-weight:700;line-height:1}
.ask-intro{left:300px;top:70px;font-family:'Roboto Condensed',sans-serif;font-size:28px;color:var(--ink)}
.role{position:absolute;white-space:nowrap}
.role--doctor{left:235px;top:44px;font-size:44px}
.role--nurse{left:295px;top:93px;font-size:51px}
.role--pharm{left:199px;top:141px;font-size:40px}
.role--rep{left:243px;top:183px;font-size:30px}
.pitch{left:358px;top:286px;width:340px;margin-left:-170px;text-align:center;font-family:'Roboto Condensed',sans-serif;font-size:21px;line-height:25px;color:var(--ink)}
.pitch strong{display:block;font-size:26px;margin-top:3px}
.back .url-button{left:133px;top:393px;width:373px;height:76px;font-size:23px}
.audience{width:170px;text-align:center}
.audience svg{display:block;margin:0 auto}
.audience p{font-family:'Roboto Condensed',sans-serif;font-size:14px;line-height:16px;color:var(--ink);margin-top:2px}
.back .socials{right:40px;top:698px;text-align:right}
.back .socials li{justify-content:flex-end}
</style>
</head>
<body>
<div class="canvas">

  <section class="side side--front front">
    <div class="abs front-sheet">
      <div class="abs workspace-photo" role="img" aria-label="Top-down photo of a doctor typing on a laptop at a white desk with stethoscope, clipboard and phone"></div>

      <div class="abs brand">
        <span class="brand-dot"></span>
        <span class="brand-name">Varenta</span>
      </div>
      <div class="abs tagline-top">healthcare</div>
      <div class="abs tagline">Malaysia's #1<span class="slash">/</span>job site</div>

      <div class="abs url-button">www.varenta-jobs.example</div>
      <svg class="abs cursor" style="left:492px;top:488px" viewBox="0 0 40 46" aria-hidden="true">
        <path d="M6 2 L6 36 L14 28 L20 42 L27 39 L21 25 L33 25 Z" fill="var(--green)" stroke="#1d1d1d" stroke-width="2" stroke-linejoin="round"/>
      </svg>

      <svg class="abs front-waves" viewBox="0 0 552 242" preserveAspectRatio="none" aria-hidden="true">
        <path d="M320 30 Q440 -8 552 8 L552 242 L420 242 Z" fill="var(--teal)"/>
        <path d="M0 18 Q180 0 360 22 L360 130 Q200 104 0 108 Z" fill="var(--green)"/>
      </svg>

      <div class="abs quote">
        <div class="q1">“Find your next</div>
        <div class="q2">Healthcare JOB!</div>
        <div class="q3">IT’S EASY!”</div>
      </div>

      <div class="abs steps">
        <div class="step" style="left:44px;top:18px"><span class="num">1</span><span class="label">CREATE<br>PROFILE</span></div>
        <div class="step" style="left:20px;top:78px"><span class="num">2</span><span class="label">SEARCH<br>JOBS</span></div>
        <div class="step" style="left:50px;top:134px"><span class="num">3</span><span class="label">APPLY!</span></div>
      </div>

      <div class="abs seeker-photo" role="img" aria-label="Photo of a smiling Asian woman doctor in a white coat looking through binoculars"></div>

      <ul class="abs socials">
        <li><span class="chip chip--web"></span>www.varenta-jobs.example</li>
        <li><span class="chip chip--fb"></span>Varenta</li>
        <li><span class="chip chip--in"></span>varentajobs</li>
        <li><span class="chip chip--ig"></span>@varentajobs</li>
        <li><span class="chip chip--gp"></span>Varenta Asia</li>
      </ul>
    </div>
  </section>

  <section class="side side--back back">
    <div class="abs back-sheet">
      <div class="photo photo--pharmacist" role="img" aria-label="Photo of a pharmacist in a white coat standing by pharmacy shelves"></div>
      <div class="photo photo--lab" role="img" aria-label="Photo of a masked lab scientist looking into a microscope"></div>
      <div class="photo photo--doctor" role="img" aria-label="Photo of a smiling doctor with a stethoscope holding a tablet"></div>
      <div class="photo photo--xray" role="img" aria-label="Photo of two women doctors in headscarves reviewing a chest X-ray"></div>

      <div class="abs ask-intro">Are you a</div>
      <div class="abs ask" style="left:0;top:66px;width:552px">
        <span class="role role--doctor">DOCTOR?</span>
        <span class="role role--nurse">NURSE?</span>
        <span class="role role--pharm">PHARMACIST?</span>
        <span class="role role--rep">MEDICAL SALES REP?</span>
      </div>

      <div class="abs pitch">
        If you’re interested<br>in a Healthcare Job —<br>We’re here to grow your
        <strong>CAREER!</strong>
      </div>

      <div class="abs url-button">www.varenta-jobs.example</div>
      <svg class="abs cursor" style="left:488px;top:452px" viewBox="0 0 40 46" aria-hidden="true">
        <path d="M6 2 L6 36 L14 28 L20 42 L27 39 L21 25 L33 25 Z" fill="var(--green)" stroke="#1d1d1d" stroke-width="2" stroke-linejoin="round"/>
      </svg>

      <div class="abs audience" style="left:232px;top:508px">
        <svg width="110" height="110" viewBox="0 0 110 110" aria-hidden="true">
          <defs><path id="arcEmp" d="M15 60 A40 40 0 0 1 95 60"/></defs>
          <text font-family="Roboto Condensed, sans-serif" font-weight="700" font-size="15" fill="var(--teal)"><textPath href="#arcEmp" startOffset="50%" text-anchor="middle">EMPLOYERS</textPath></text>
          <circle cx="55" cy="70" r="36" fill="var(--teal)"/>
          <circle cx="55" cy="60" r="9" fill="var(--green)"/>
          <path d="M37 90 Q37 72 55 72 Q73 72 73 90 Z" fill="var(--green)"/>
        </svg>
        <p>We’ve made Talent Recruitment more convenient and time efficient for you.</p>
      </div>

      <div class="abs audience" style="left:384px;top:496px">
        <svg width="110" height="122" viewBox="0 0 110 122" aria-hidden="true">
          <defs><path id="arcJob" d="M15 72 A40 40 0 0 1 95 72"/></defs>
          <text font-family="Roboto Condensed, sans-serif" font-weight="700" font-size="15" fill="var(--teal)"><textPath href="#arcJob" startOffset="50%" text-anchor="middle">JOBSEEKERS</textPath></text>
          <circle cx="55" cy="82" r="36" fill="var(--green)"/>
          <circle cx="46" cy="74" r="8" fill="var(--teal)"/>
          <path d="M30 100 Q30 84 46 84 Q62 84 62 100 Z" fill="var(--teal)"/>
          <circle cx="66" cy="70" r="8" fill="var(--teal-dark)"/>
          <path d="M52 98 Q52 80 66 80 Q80 80 80 98 Z" fill="var(--teal-dark)"/>
        </svg>
        <p>In just 3 easy steps, find your dream Healthcare job!</p>
      </div>

      <ul class="abs socials">
        <li>www.varenta-jobs.example<span class="chip chip--web"></span></li>
        <li>Varenta<span class="chip chip--fb"></span></li>
        <li>varentajobs<span class="chip chip--in"></span></li>
        <li>@varentajobs<span class="chip chip--ig"></span></li>
        <li>Varenta Asia<span class="chip chip--gp"></span></li>
      </ul>
    </div>
  </section>

</div>
</body>
</html>
```